Design Creative Banner or Gif Ads. 3 Designs To Be Selected

Come up with some creative banner ads for stonewell.co.nz

*At least 3 different winning banners will be chosen*

Please provide banner ads / gif ads in common google ads / website banner formats.

They can be gif or static but must stand out while still maintaining clear clean text and visuals, with a premium professional feel (please avoid clip art or anything that gives a cheap message).

Please keep in mind that these will likely be small ads so text needs to be large and if there's there a lot of text then use multiple frames/ pages as submit as a gif.

Style
Minimal & clean lines
Architectural or realistic images
Avoid cartoon styles, clipart, or anything that looks cheap

Font
Nexa or Montserrat or similar

Tone
Premium, serious, trustworthy — fits new builds

Colours
Option 1: Deep Navy (trust & quality) & lighter blues and warm grey
Option 2: Open to bright colours to help the ads stand out, such as (but not limited to) bright pink with black, yellow, fluorescent green, provided the messaging is still done professionally.
Our logo is attached (Stone Well Logo)

Display Sizes
Ad specs for file sizes should be file formats like JPEG, GIF, and PNG, with animations limited to a max of 30 seconds or less.
We will need several different ad sizes provided for each of the 3 selected winning designs.

• Medium Rectangle: 300 × 250 pixels
• Leaderboard: 728 × 90 pixels
• Desktop Banner ad image: (640x360 pixels)
• Desktop Banner ad image 2: (300x600 pixels)
• Possibly one or two other sizes

Flexibility to be creative
The ad text, words, upper/lower case, layout, colour, theme, and images can be adjusted to how you think it will look best. The follow example ads are just examples of what we are after but we are keen to see what you can create.

Recommendations at this point:
1. Avoid text heavy
2. Looking for more Gif ads
3. Imaging: if possible use real stock photo's rather than AI

Themes:

1
Building Soon? Start Here
Free Build Planning Pack:
✓ Build Cost Calculator
✓ Hidden Cost Checklist
✓ Builder Comparison Guide
Build With Confidence
Download Free

2
Before You Choose A Builder
Compare Price, Scope, Risk & Value
Avoid Costly Mistakes
Choose The Right Builder With Confidence
Download The Free Guide

3
Planning A New Build?
Avoid These Common Mistakes:
✗ Hidden Exclusions
✗ Missing Scope
✗ Unrealistic Allowances
✗ Budget Blowouts
Download The Free Guide

4
Before You Buy Land
Know what it could cost to build.
Avoid Costly Building Mistakes
Download Our Free Guides

5
Know Your Build Budget?
• Free Build Cost Calculator
• Hidden Cost Checklist
• Build Planning Tools
Calculate Costs (Download)

Target Market(s)

Landowners looking to build

Industry/Entity Type

Building

Font styles to use
Other font styles liked:
• Nexa or Montserrat or similar

Requirements
Should not have
• Avoid cartoon styles, clipart, or anything that looks cheap

```html
<!DOCTYPE html>
<html lang="en">
<head>
<meta charset="utf-8">
<title>Stone Well – Building Soon? Start Here</title>
<link rel="stylesheet" href="https://fonts.googleapis.com/css2?family=Montserrat:wght@400;600;700;800;900&display=swap">
<style>
  :root {
    --wall-grey: #97958d;
    --wall-light: #a3a19a;
    --box-tan: #c69c74;
    --box-shadow: #5b4638;
    --white: #ffffff;
    --ink: #0a0a0a;
    --accent-red: #ff0000;
    --highlight-yellow: #fff200;
    --cta-red-top: #e00000;
    --cta-red-bottom: #a80000;
    --cta-text: #fff6ea;
  }
  * { margin: 0; padding: 0; box-sizing: border-box; }
  html, body { width: 1200px; height: 675px; overflow: hidden; background: var(--wall-grey); }
  body { font-family: "Montserrat", Arial, sans-serif; }

  .banner {
    position: relative;
    width: 1200px;
    height: 675px;
    overflow: hidden;
    background: var(--wall-grey);
  }

  .hero-photo {
    position: absolute;
    inset: 0;
    background:
      radial-gradient(ellipse 420px 260px at 880px 520px, var(--box-shadow) 0%, rgba(91,70,56,0.55) 45%, rgba(91,70,56,0) 100%),
      linear-gradient(160deg, rgba(198,156,116,0) 45%, rgba(198,156,116,0.85) 62%, var(--box-tan) 100%),
      linear-gradient(90deg, var(--wall-grey) 0%, var(--wall-light) 60%, var(--wall-grey) 100%);
  }

  .headline {
    position: absolute;
    left: 32px;
    top: -18px;
    font-size: 139px;
    font-weight: 800;
    letter-spacing: -3px;
    color: var(--white);
    line-height: 1.15;
    white-space: nowrap;
  }

  .subhead {
    position: absolute;
    left: 63px;
    top: 136px;
    font-size: 72px;
    font-weight: 800;
    color: var(--ink);
    letter-spacing: 0;
    line-height: 1.2;
  }

  .pack-title {
    position: absolute;
    left: 64px;
    top: 247px;
    font-size: 31px;
    font-weight: 700;
    color: var(--ink);
    display: flex;
    align-items: center;
    gap: 6px;
    white-space: nowrap;
  }
  .pack-title .free-tag {
    background: var(--highlight-yellow);
    color: var(--accent-red);
    padding: 0 5px;
    line-height: 31px;
  }

  .pack-list {
    position: absolute;
    left: 69px;
    top: 290px;
    list-style: none;
  }
  .pack-list li {
    display: flex;
    align-items: center;
    font-size: 30px;
    font-weight: 400;
    color: var(--ink);
    line-height: 38px;
    white-space: nowrap;
  }
  .pack-list li::before {
    content: "";
    width: 11px;
    height: 11px;
    background: var(--highlight-yellow);
    margin-right: 13px;
    flex-shrink: 0;
  }

  .tagline {
    position: absolute;
    left: 70px;
    top: 418px;
    font-size: 80px;
    font-weight: 800;
    line-height: 70px;
    color: var(--white);
    letter-spacing: -1px;
  }
  .tagline .accent { color: var(--accent-red); }

  .brand {
    position: absolute;
    left: 700px;
    top: 184px;
    display: flex;
    align-items: center;
    gap: 14px;
  }
  .brand-mark {
    width: 50px;
    height: 45px;
    background: var(--white);
  }
  .brand-name {
    font-size: 25px;
    font-weight: 600;
    color: var(--white);
    line-height: 1;
  }
  .brand-tagline {
    font-size: 6.4px;
    font-weight: 700;
    color: var(--white);
    letter-spacing: 0.1px;
    margin-top: 6px;
    white-space: nowrap;
  }

  .cta-button {
    position: absolute;
    left: 804px;
    top: 555px;
    width: 361px;
    height: 81px;
    border: 2px solid var(--white);
    border-radius: 20px;
    background: linear-gradient(180deg, var(--cta-red-top) 0%, var(--cta-red-bottom) 100%);
    color: var(--cta-text);
    font-size: 33px;
    font-weight: 700;
    letter-spacing: 1px;
    display: flex;
    align-items: center;
    justify-content: center;
    text-decoration: none;
  }
</style>
</head>
<body>
  <main class="banner">
    <div class="hero-photo" role="img" aria-label="Photo of a man curled up inside a cardboard box against a grey wall, with a roof shape chalked above the box"></div>

    <h1 class="headline">Building Soon?</h1>
    <h2 class="subhead">START HERE</h2>

    <p class="pack-title"><span class="free-tag">Free</span>Build Planning Pack:</p>
    <ul class="pack-list">
      <li>Build Cost Calculator</li>
      <li>Hidden Cost Checklist</li>
      <li>Builder Comparison Guide</li>
    </ul>

    <p class="tagline">Build<br><span class="accent">With</span><br>Confidence</p>

    <div class="brand">
      <div class="brand-mark"></div>
      <div class="brand-text">
        <div class="brand-name">Stone Well</div>
        <div class="brand-tagline">COMPARE QUOTES FROM TRUSTED BUILDERS</div>
      </div>
    </div>

    <a class="cta-button" href="#">DOWNLOAD FREE</a>
  </main>
</body>
</html>
```